Vel Framewright - Worpress Design

We are a consultancy to help builders to optimize their planning in order to save building costs. For that reason we need a website to offer our services, present our history, the mission and offer a plug-in for a first contact (including calendar), testimonials, a blog etc.
As an idea, I really like: https://www.kestrumadvisory.de/
Later on the website should be programmed in www.wolkanet.de in our Wordpress area. The text, of course, will be done by myself. The colors should be suitable to our recently designed logo.

```html
<!DOCTYPE html>
<html lang="en">
<head>
<meta charset="utf-8">
<title>Vel Framewright</title>
<link href="https://fonts.googleapis.com/css2?family=Montserrat:ital,wght@0,300;0,400;0,500;0,600;0,700;1,700&display=swap" rel="stylesheet">
<style>
:root{
  --ink:#1d1d1d;
  --text:#6b6b6b;
  --gold:#c08a36;
  --gold-light:#dcb35c;
  --brown:#b97a2f;
  --cream:#f7efe8;
  --dark:#2b2b2b;
  --line:#d9a866;
  --white:#ffffff;
}
*{margin:0;padding:0;box-sizing:border-box}
html,body{width:1200px;height:5188px;overflow:hidden}
body{position:relative;background:var(--white);font-family:'Montserrat',sans-serif;color:var(--ink)}
.abs{position:absolute}
.photo{position:absolute;overflow:hidden}
.btn{position:absolute;display:flex;align-items:center;justify-content:center;background:linear-gradient(90deg,#b8842e,var(--gold-light),#b8842e);color:var(--ink);font-size:11px;font-weight:600;text-decoration:none}
.para{font-size:11.5px;line-height:23px;color:var(--text)}

/* header */
.brand{font-weight:700;font-size:22px;letter-spacing:1px;color:var(--gold);display:flex;align-items:center;gap:10px}
.brand-mark{width:26px;height:26px;border:2px solid var(--gold)}
.nav{position:absolute;top:44px;font-size:11.5px;color:#555}
.nav a{position:absolute;color:#555;text-decoration:none;white-space:nowrap}

/* photo areas */
.photo-team{
  background:
    radial-gradient(ellipse 18% 22% at 42% 34%, rgba(122,36,48,.75), transparent 70%),
    radial-gradient(ellipse 16% 20% at 84% 38%, rgba(60,52,50,.7), transparent 70%),
    radial-gradient(ellipse 14% 18% at 22% 40%, rgba(150,110,90,.55), transparent 70%),
    radial-gradient(ellipse 60% 30% at 55% 92%, rgba(40,44,52,.85), transparent 75%),
    linear-gradient(90deg,#8a8f93 0%,#c9ccce 18%,#7b8187 30%,#d6d8d8 48%,#8d9297 62%,#cfd1d0 80%,#878c91 100%);
}
.photo-about{
  background:
    radial-gradient(ellipse 28% 40% at 28% 58%, rgba(130,160,200,.85), transparent 70%),
    radial-gradient(ellipse 16% 16% at 36% 30%, rgba(190,140,110,.8), transparent 70%),
    radial-gradient(ellipse 26% 38% at 70% 66%, rgba(228,170,160,.85), transparent 70%),
    radial-gradient(ellipse 16% 18% at 66% 28%, rgba(214,168,110,.85), transparent 70%),
    radial-gradient(ellipse 40% 14% at 60% 96%, rgba(70,60,55,.6), transparent 75%),
    linear-gradient(120deg,#ece9e4,#f4f2ee 45%,#dcd7d0);
}
.photo-work{
  background:
    radial-gradient(ellipse 14% 20% at 80% 14%, rgba(210,90,150,.45), transparent 70%),
    radial-gradient(ellipse 12% 18% at 90% 8%, rgba(150,200,60,.5), transparent 70%),
    radial-gradient(ellipse 18% 26% at 60% 42%, rgba(150,110,90,.8), transparent 70%),
    radial-gradient(ellipse 16% 24% at 74% 44%, rgba(190,185,185,.8), transparent 70%),
    radial-gradient(ellipse 30% 26% at 66% 82%, rgba(60,65,72,.55), transparent 75%),
    linear-gradient(100deg,#a9aeb2 0%,#e4e6e6 25%,#f3f4f3 55%,#e1e3e2 100%);
}
.photo-support{
  background:
    radial-gradient(ellipse 30% 40% at 30% 38%, rgba(40,30,28,.9), transparent 70%),
    radial-gradient(ellipse 16% 18% at 40% 40%, rgba(225,180,150,.9), transparent 70%),
    radial-gradient(ellipse 30% 38% at 32% 82%, rgba(240,236,232,.95), transparent 72%),
    radial-gradient(ellipse 14% 30% at 14% 80%, rgba(170,50,45,.6), transparent 70%),
    linear-gradient(90deg,#6f6058 0%,#b8aa9e 30%,#ebe4dc 60%,#f6f2ed 100%);
}
.thumb-1{background:
    radial-gradient(ellipse 30% 40% at 70% 40%, rgba(220,140,60,.8), transparent 70%),
    radial-gradient(ellipse 30% 30% at 30% 80%, rgba(70,110,150,.6), transparent 70%),
    linear-gradient(135deg,#8c9aa6,#d9cfc2)}
.thumb-2{background:
    radial-gradient(ellipse 30% 30% at 60% 70%, rgba(220,200,170,.8), transparent 70%),
    linear-gradient(135deg,#f2f0ec,#c8c2b8)}
.thumb-3{background:
    radial-gradient(ellipse 30% 40% at 60% 40%, rgba(60,66,76,.7), transparent 70%),
    linear-gradient(135deg,#e2e4e6,#9ba0a6)}

/* hero */
.hero-title{left:125px;top:168px;font-size:62px;line-height:62px;font-weight:400;letter-spacing:.5px;z-index:2}
.connector{position:absolute;background:var(--line)}
.section-title{font-weight:400;color:var(--ink)}

/* services */
.services-panel{left:0;top:1606px;width:670px;height:723px;background:var(--brown);border-radius:0 48px 48px 0;color:var(--white)}
.services-panel h2{position:absolute;left:125px;top:72px;font-size:60px;font-weight:400}
.services-panel p{position:absolute;left:125px;top:168px;width:460px;font-size:11px;line-height:23.5px;color:#fbeee0}
.service-item{position:absolute;left:125px;font-size:20px;line-height:26px;font-weight:700}

/* blogs */
.blog-card{position:absolute;top:2428px;width:274px;height:346px;background:var(--white);box-shadow:0 4px 18px rgba(0,0,0,.08);overflow:hidden}
.blog-card .thumb{position:absolute;left:0;top:0;width:100%;height:215px}
.blog-card h3{position:absolute;left:28px;top:248px;width:160px;font-size:13.5px;line-height:22px;font-weight:700}
.blog-card .go{position:absolute;left:218px;top:260px;width:32px;height:32px;border-radius:50%;background:var(--gold);display:flex;align-items:center;justify-content:center}

/* testimonials */
.testimonials{left:0;top:2873px;width:1200px;height:928px;background:var(--cream)}
.testimonials h2{position:absolute;top:92px;width:100%;text-align:center;font-size:48px;line-height:58px;font-weight:400}
.t-col{position:absolute;top:257px;width:227px;display:flex;flex-direction:column;gap:16px}
.t-card{background:var(--white);border-radius:6px;padding:22px 26px 20px}
.t-head{display:flex;align-items:center;gap:12px;margin-bottom:16px}
.avatar{width:30px;height:30px;border-radius:50%;flex:none}
.t-name{font-size:13px;font-style:italic;font-weight:700}
.t-role{font-size:7px;color:#999}
.t-card p{font-size:10px;line-height:17px;color:var(--text)}
.stars{margin-top:14px;color:#f2b705;font-size:13px;letter-spacing:6px}

/* contact */
.contact-card{left:533px;top:3972px;width:542px;height:561px;background:var(--white);border-radius:24px;box-shadow:0 6px 30px rgba(0,0,0,.1)}
.contact-card h2{position:absolute;left:71px;top:52px;font-size:46px;line-height:52px;font-weight:400}
.field{position:absolute;left:71px;width:400px;border:1px solid #cfcfcf;font-size:11px;color:#888;padding:0 30px;display:flex;align-items:center}

/* footer */
.footer{left:0;top:4706px;width:1200px;height:393px;background:var(--dark);color:var(--white)}
.footer-nav a{position:absolute;top:210px;font-size:12px;color:#ddd;text-decoration:none}
.f-contact{position:absolute;top:270px;display:flex;align-items:center;gap:16px;font-size:11.5px;color:#eee}
.f-icon{width:38px;height:38px;border-radius:50%;border:1px solid #888;display:flex;align-items:center;justify-content:center}
.copyright{position:absolute;left:0;top:5133px;width:1200px;text-align:center;font-size:12px;color:#555}
</style>
</head>
<body>

<header>
  <div class="abs brand" style="left:125px;top:32px"><span class="brand-mark"></span>VEL FRAMEWRIGHT</div>
  <nav class="nav">
    <a href="#" style="left:662px">Home</a>
    <a href="#" style="left:743px">About us</a>
    <a href="#" style="left:839px">Services</a>
    <a href="#" style="left:930px">Testimonial</a>
    <a href="#" style="left:1041px">Blogs</a>
  </nav>
</header>

<section class="hero">
  <div class="photo photo-team" role="img" aria-label="Team meeting in a bright office with large windows" style="left:447px;top:121px;width:753px;height:646px;border-radius:0 0 0 48px"></div>
  <h1 class="abs hero-title section-title">Innovate Solution<br>For Business<br>Success</h1>
  <p class="abs para" style="left:125px;top:388px;width:285px">Lorem Ipsum is simply dummy text of the printing and typesetting industry. Lorem Ipsum has been the industry's standard dummy text ever since the 1500s.</p>
  <a class="btn" href="#" style="left:125px;top:513px;width:141px;height:43px">Contact</a>
</section>

<div class="connector" style="left:338px;top:668px;width:1px;height:187px"></div>
<div class="connector" style="left:338px;top:668px;width:109px;height:1px"></div>
<div class="connector" style="left:769px;top:767px;width:1px;height:119px"></div>
<div class="connector" style="left:584px;top:936px;width:40px;height:1px"></div>

<section class="about">
  <div class="photo photo-about" role="img" aria-label="Two colleagues reviewing a clipboard together" style="left:0;top:855px;width:584px;height:594px;border-radius:0 48px 48px 0"></div>
  <h2 class="abs section-title" style="left:648px;top:900px;font-size:62px;line-height:62px">About Vel<br>Framewright</h2>
  <p class="abs para" style="left:648px;top:1050px;width:425px">Lorem Ipsum is simply dummy text of the printing and typesetting industry. Lorem Ipsum has been the industry's standard dummy text ever since the 1500s.</p>
  <h3 class="abs" style="left:648px;top:1145px;font-size:21px;font-weight:600">Our Mission</h3>
  <p class="abs para" style="left:648px;top:1188px;width:425px">Lorem Ipsum is simply dummy text of the printing and typesetting industry. Lorem Ipsum has been the industry's standard dummy text ever since the 1500s, when an unknown printer took a galley of type and scrambled it to make a type specimen book. It has survived not only five centuries, but also the leap into electronic typesetting, remaining essentially unchanged.</p>
  <a class="btn" href="#" style="left:648px;top:1361px;width:141px;height:40px">Read More</a>
</section>

<section class="services">
  <div class="photo photo-work" role="img" aria-label="Two colleagues working at a laptop in a bright office with sticky notes" style="left:221px;top:1534px;width:979px;height:636px;border-radius:48px 0 0 0"></div>
  <div class="abs services-panel">
    <h2>Our Serives</h2>
    <p>Lorem Ipsum is simply dummy text of the printing and typesetting industry. Lorem Ipsum has been the industry's standard dummy text ever since the 1500s, when an unknown printer took a galley of type and scrambled it to make a type specimen book. It has survived not only five centuries, but also the leap into electronic typesetting, remaining essentially unchanged.</p>
    <div class="service-item" style="top:347px">Coaching &amp; Training<br>Provider</div>
    <div class="service-item" style="top:427px">Management<br>Consultancies</div>
    <div class="service-item" style="top:509px">Agency Service Provider</div>
    <div class="service-item" style="top:564px">Expert Services</div>
    <div class="service-item" style="top:619px">IT Service Provider</div>
  </div>
</section>

<section class="blogs">
  <h2 class="abs section-title" style="left:125px;top:2452px;font-size:48px;line-height:56px">THE LATEST<br>BLOGS</h2>
  <p class="abs" style="left:125px;top:2586px;width:285px;font-size:13px;line-height:23px;font-weight:500;color:#444">Lorem Ipsum is simply dummy text of the printing and typesetting industry. Lorem Ipsum has been the industry's standard dummy text ever since the 1500s, when an unknown printer took a galley of type and scrambled it to make a type specimen book</p>

  <article class="blog-card" style="left:507px">
    <div class="thumb thumb-1" role="img" aria-label="Team gathered around a table"></div>
    <h3>SEARCHLY'S NEW PPC FEATURES ARE LOADED WITH AI</h3>
    <span class="go"><svg width="14" height="14" viewBox="0 0 14 14"><path d="M3 11L11 3M5 3h6v6" stroke="#fff" stroke-width="1.6" fill="none"/></svg></span>
  </article>
  <article class="blog-card" style="left:805px">
    <div class="thumb thumb-2" role="img" aria-label="Desk with laptop by a window"></div>
    <h3>HOW SEARCHLY KILLED THE BROAD MATCH KEYWORD?</h3>
    <span class="go"><svg width="14" height="14" viewBox="0 0 14 14"><path d="M3 11L11 3M5 3h6v6" stroke="#fff" stroke-width="1.6" fill="none"/></svg></span>
  </article>
  <article class="blog-card" style="left:1105px">
    <div class="thumb thumb-3" role="img" aria-label="Computer screen on a desk"></div>
    <h3>THE 9 RULES OF SOCIAL MEDIA ENGAGEMENT</h3>
  </article>
</section>

<section class="abs testimonials">
  <h2>WHAT OUR CLIENT<br>SAYS</h2>

  <div class="t-col" style="left:125px">
    <div class="t-card">
      <div class="t-head"><span class="avatar" role="img" aria-label="Client portrait" style="background:#b8a592"></span><div><div class="t-name">Tomas Reyes</div><div class="t-role">Business Name</div></div></div>
      <p>Lorem Ipsum is simply dummy text of the printing and typesetting industry. Lorem Ipsum has been the industry's standard dummy text ever since the 1500s.</p>
      <div class="stars">★★★★★</div>
    </div>
    <div class="t-card">
      <div class="t-head"><span class="avatar" role="img" aria-label="Client portrait" style="background:#c49355"></span><div><div class="t-name">Tomas Reyes</div><div class="t-role">Business Name</div></div></div>
      <p>Lorem Ipsum is simply dummy text of the printing and typesetting industry. Lorem Ipsum has been the industry's standard dummy text ever since the 1500s, when an unknown printer took a galley of type and scrambled it to make a type specimen book. It has survived not only five centuries, but also the leap into electronic</p>
      <div class="stars">★★★★★</div>
    </div>
  </div>

  <div class="t-col" style="left:366px">
    <div class="t-card">
      <div class="t-head"><span class="avatar" role="img" aria-label="Client portrait" style="background:#8e969e"></span><div><div class="t-name">Tomas Reyes</div><div class="t-role">Business Name</div></div></div>
      <p>Lorem Ipsum is simply dummy text of the printing and typesetting industry. Lorem Ipsum has been the industry's standard dummy text ever since the 1500s, when an unknown printer took a galley of type and scrambled it to make a type specimen book. It has survived not only five centuries, but also the leap into electronic</p>
      <div class="stars">★★★★★</div>
    </div>
    <div class="t-card">
      <div class="t-head"><span class="avatar" role="img" aria-label="Client portrait" style="background:#a3aab0"></span><div><div class="t-name">Tomas Reyes</div><div class="t-role">Business Name</div></div></div>
      <p>Lorem Ipsum is simply dummy text of the printing and typesetting industry. Lorem Ipsum has been the industry's standard dummy text ever since the 1500s.</p>
      <div class="stars">★★★★★</div>
    </div>
  </div>

  <div class="t-col" style="left:606px">
    <div class="t-card">
      <div class="t-head"><span class="avatar" role="img" aria-label="Client portrait" style="background:#d4a23c"></span><div><div class="t-name">Tomas Reyes</div><div class="t-role">Business Name</div></div></div>
      <p>Lorem Ipsum is simply dummy text of the printing and typesetting industry. Lorem Ipsum has been the industry's standard dummy text ever since the 1500s.</p>
      <div class="stars">★★★★★</div>
    </div>
    <div class="t-card">
      <div class="t-head"><span class="avatar" role="img" aria-label="Client portrait" style="background:#d9b8a4"></span><div><div class="t-name">Tomas Reyes</div><div class="t-role">Business Name</div></div></div>
      <p>Lorem Ipsum is simply dummy text of the printing and typesetting industry. Lorem Ipsum has been the industry's standard dummy text ever since the 1500s, when an unknown printer took a galley of type and scrambled it to make a type specimen book. It has survived not only five centuries, but also the leap into electronic</p>
      <div class="stars">★★★★★</div>
    </div>
  </div>

  <div class="t-col" style="left:847px">
    <div class="t-card">
      <div class="t-head"><span class="avatar" role="img" aria-label="Client portrait" style="background:#7f8389"></span><div><div class="t-name">Tomas Reyes</div><div class="t-role">Business Name</div></div></div>
      <p>Lorem Ipsum is simply dummy text of the printing and typesetting industry. Lorem Ipsum has been the industry's standard dummy text ever since the 1500s, when an unknown printer took a galley of type and scrambled it to make a type specimen book. It has survived not only five centuries, but also the leap into electronic</p>
      <div class="stars">★★★★★</div>
    </div>
    <div class="t-card">
      <div class="t-head"><span class="avatar" role="img" aria-label="Client portrait" style="background:#c58b45"></span><div><div class="t-name">Tomas Reyes</div><div class="t-role">Business Name</div></div></div>
      <p>Lorem Ipsum is simply dummy text of the printing and typesetting industry. Lorem Ipsum has been the industry's standard dummy text ever since the 1500s.</p>
      <div class="stars">★★★★★</div>
    </div>
  </div>
</section>

<section class="contact">
  <div class="photo photo-support" role="img" aria-label="Support agent wearing a headset by a bright window" style="left:125px;top:3899px;width:787px;height:705px;border-radius:40px"></div>
  <div class="abs contact-card">
    <h2>GET IN TOUCH<br>WITH US</h2>
    <div class="field" style="top:187px;height:48px">Name</div>
    <div class="field" style="top:249px;height:49px">Email</div>
    <div class="field" style="top:312px;height:195px;align-items:flex-start;padding-top:18px">Message</div>
    <svg class="abs" style="left:422px;top:458px" width="32" height="30" viewBox="0 0 32 30"><path d="M2 14L30 2L22 28L15 18Z" fill="#c08a36"/><path d="M15 18L30 2" stroke="#fff" stroke-width="1.5"/></svg>
  </div>
</section>

<footer class="abs footer">
  <div class="abs brand" style="left:0;top:98px;width:1200px;justify-content:center;color:#fff"><span class="brand-mark" style="border-color:#fff"></span>VEL FRAMEWRIGHT</div>
  <nav class="footer-nav">
    <a href="#" style="left:332px">Home</a>
    <a href="#" style="left:415px">About us</a>
    <a href="#" style="left:518px">Services</a>
    <a href="#" style="left:614px">Testimonial</a>
    <a href="#" style="left:733px">Blogs</a>
    <a href="#" style="left:813px">Contact</a>
  </nav>
  <div class="f-contact" style="left:182px"><span class="f-icon"><svg width="14" height="14" viewBox="0 0 14 14"><path d="M3 1l2 3-1.5 1.5a8 8 0 004 4L9 8l3 2-1 3C6 13 1 8 1 3z" fill="#fff"/></svg></span>555-014-2730</div>
  <div class="f-contact" style="left:436px"><span class="f-icon"><svg width="12" height="14" viewBox="0 0 12 14"><path d="M6 13S1 8 1 5a5 5 0 0110 0c0 3-5 8-5 8z" fill="#fff"/><circle cx="6" cy="5" r="1.8" fill="#2b2b2b"/></svg></span>Lorem ipsum is dummy, NJ 07010</div>
  <div class="f-contact" style="left:806px"><span class="f-icon"><svg width="14" height="10" viewBox="0 0 14 10"><rect width="14" height="10" rx="1" fill="#fff"/><path d="M1 1l6 5 6-5" stroke="#2b2b2b" fill="none"/></svg></span>SALES@VELFRAMEWRIGHT.COM</div>
</footer>
<p class="copyright">© 2016-2023 - Vel Framewright</p>

</body>
</html>
```